Looking for a clean, modern, and professional business card design that reflects Valtrim Systems

The design should include the company logo, contact details, and align with our brand identity. Please use a sophisticated and minimalist style, incorporating [specific colors, if applicable]. Creativity is welcome, but the card must maintain a polished and professional appearance.

Details to Include:

Name: Gavin Trelowe
Title: VP Sales / Operations
Company: Valtrim Systems
Phone: 483.216.7705
Email: gavin@valtrimsystems-example.com
Website: www.valtrimsystems-example.com

```html
<!DOCTYPE html>
<html lang="en">
<head>
<meta charset="utf-8">
<title>Valtrim Systems – Business Card</title>
<link href="https://fonts.googleapis.com/css2?family=Lato:ital,wght@0,300;0,400;0,700;0,900;1,300&display=swap" rel="stylesheet">
<style>
  :root {
    --stage: #2a2b2e;
    --card-white: #ffffff;
    --card-dark: #222326;
    --card-dark-soft: #2b2c30;
    --ink: #1b1b1d;
    --brand-blue: #3a78c3;
    --muted: #6d6e72;
    --light: #f2f2f2;
  }
  * { box-sizing: border-box; margin: 0; padding: 0; }
  html, body {
    width: 1200px; height: 952px; overflow: hidden;
    background: var(--stage);
    font-family: "Lato", Arial, sans-serif;
  }
  .stage {
    position: relative; width: 1200px; height: 952px;
  }
  .card {
    position: absolute; left: 240px; width: 720px; height: 411px;
    box-shadow: 0 12px 30px rgba(0,0,0,.45);
  }
  .card--front { top: 45px; background: var(--card-white); }
  .card--back { top: 496px; background: var(--card-dark); overflow: hidden; }

  .wordmark {
    font-weight: 900; letter-spacing: 2px; text-transform: uppercase;
    display: flex; align-items: center; gap: 14px;
  }
  .wordmark__square { width: 22px; height: 22px; background: var(--brand-blue); }
  .card--front .wordmark {
    position: absolute; top: 70px; left: 0; right: 0; justify-content: center;
    color: var(--ink); font-size: 40px;
  }

  .identity { position: absolute; left: 70px; top: 200px; }
  .identity__name {
    font-size: 30px; font-weight: 900; text-transform: uppercase; color: var(--brand-blue);
    letter-spacing: .5px;
  }
  .identity__title {
    margin-top: 4px; font-size: 19px; font-weight: 300; font-style: italic; color: var(--muted);
  }

  .contacts { position: absolute; left: 385px; top: 196px; list-style: none; }
  .contacts li {
    display: flex; align-items: center; gap: 12px;
    font-size: 16px; color: var(--muted); margin-bottom: 12px;
  }
  .contacts .icon {
    width: 22px; height: 22px; background: var(--ink); border-radius: 3px;
    display: flex; align-items: center; justify-content: center; flex: none;
  }
  .rule {
    position: absolute; left: 0; right: 0; bottom: 52px; height: 2px; background: var(--brand-blue);
  }

  .back-texture {
    position: absolute; inset: 0;
    background: radial-gradient(ellipse at 50% 50%, var(--card-dark-soft), var(--card-dark) 75%);
  }
  .card--back .wordmark {
    position: absolute; inset: 0; justify-content: center;
    color: var(--light); font-size: 44px;
  }
</style>
</head>
<body>
<main class="stage">
  <section class="card card--front" aria-label="Business card front">
    <div class="wordmark"><span class="wordmark__square"></span>Valtrim Systems</div>
    <div class="identity">
      <h1 class="identity__name">Gavin Trelowe</h1>
      <p class="identity__title">VP Sales / Operations</p>
    </div>
    <ul class="contacts">
      <li><span class="icon"><svg width="13" height="13" viewBox="0 0 24 24"><path fill="#fff" d="M6.6 10.8a15 15 0 0 0 6.6 6.6l2.2-2.2a1 1 0 0 1 1-.25 11.4 11.4 0 0 0 3.6.6 1 1 0 0 1 1 1V20a1 1 0 0 1-1 1A17 17 0 0 1 3 4a1 1 0 0 1 1-1h3.5a1 1 0 0 1 1 1c0 1.25.2 2.45.6 3.6a1 1 0 0 1-.25 1z"/></svg></span>483.216.7705</li>
      <li><span class="icon"><svg width="13" height="13" viewBox="0 0 24 24"><rect x="2" y="5" width="20" height="14" fill="none" stroke="#fff" stroke-width="2"/><path d="M2 5l10 8 10-8" fill="none" stroke="#fff" stroke-width="2"/></svg></span>gavin@valtrimsystems-example.com</li>
      <li><span class="icon"><svg width="13" height="13" viewBox="0 0 24 24"><path fill="#fff" d="M5 3l14 8-6 1.5 4 7-2.5 1.5-4-7L6 18z"/></svg></span>www.valtrimsystems-example.com</li>
    </ul>
    <div class="rule"></div>
  </section>

  <section class="card card--back" aria-label="Business card back">
    <div class="back-texture" role="img" aria-label="Faint dark geometric background pattern"></div>
    <div class="wordmark"><span class="wordmark__square"></span>Valtrim Systems</div>
  </section>
</main>
</body>
</html>
```